依頼詳細
現在のサイトのコンテンツを利用してリニューアル。
パソコン版とスマホ版をお願いします。ただコンペはパソコン版のみでも可能。決定後、スマホ版の作成をお願いします。

レスポンシブウェブデザインを意識したデザインでお願いします。
参考URL、また、現在のURLは添付ファイルに記載。
メインカラーはグリーン
ワンポイントは白もしくは他の色でもOK。

また継続してサブぺージ(下層ページ)のデザインをお願いできる方は目安の単価を教えてもらえると嬉しいです。

詳細は添付したエクセルをご確認ください。
・既存サイト
・参考サイト
・フレームワーク
・ディレクトマップ

レイアウト、参考サイトは添付ファイルにいれました。
また、テンプレート・テーマを利用する場合、
下記のような記載を提案の中にいれてください。
例:WordpressテーマはCorpLumen、デザインスキンは無料のRNF2019 KX4(http://corplumen-demo.net/ex_plugin/rnfmeet2019_kx4/)をベースにデザインいたしました。
など
素材となる写真は現在、撮影中ですので、一旦他のサイトや参考URLや既存URLの写真をサンプルとして入れてください。(サンプルなどの表記をお願いします)
また、購入が必要な写真などを利用した場合、価格とサイト名を教えてください。
サイトURL
ページ数
1ページ
希望イメージ
シンプル 複雑
単色 カラフル
暗い 明るい
日常 高級
遊び心 厳粛
未来的 伝統的
女性的 男性的
希望する色
緑系
納品ファイル
• イラストレーター形式 (.ai)
• フォトショップ形式 (.psd)
• PNG形式 (.png)
補足説明
上記のいずれか1つ。アウトラインありとなしの2つ。

とても見やすく分かりやすいデザインでした。

たくさんのご提案ありがとうございました。
次回もぜひ、よろしくお願い致します。

```html
<!DOCTYPE html>
<html lang="ja">
<head>
<meta charset="utf-8">
<title>燕川たびナビ</title>
<link rel="stylesheet" href="https://fonts.googleapis.com/css2?family=Noto+Sans+JP:wght@400;500;700&family=Noto+Serif+JP:wght@600;700&display=swap">
<style>
:root{
  --green:#3f7a3a;
  --green-dark:#2f6129;
  --green-light:#e7efe4;
  --bg:#f1f1ee;
  --white:#ffffff;
  --text:#333333;
  --muted:#777777;
  --line:#d4d4cf;
  --accent:#f2c300;
}
*{margin:0;padding:0;box-sizing:border-box}
html,body{width:1200px;height:2340px;overflow:hidden}
body{background:var(--bg);color:var(--text);font-family:"Noto Sans JP",sans-serif;position:relative}
.site-header{height:110px;background:var(--white);position:relative}
.brand-sub{position:absolute;left:70px;top:12px;font-size:11px;color:var(--muted)}
.brand{position:absolute;left:70px;top:34px;display:flex;align-items:center;gap:12px}
.brand-mark{width:22px;height:22px;background:var(--green)}
.brand-name{font-weight:700;font-size:32px;line-height:1.2;color:var(--green-dark);letter-spacing:2px}
.util{position:absolute;right:70px;top:16px;display:flex;gap:14px;align-items:center;font-size:12px;color:var(--muted)}
.util .size{display:flex;gap:4px}
.util .size span{border:1px solid var(--line);padding:1px 8px;font-size:11px}
.util-links{position:absolute;right:160px;top:46px;display:flex;gap:18px;font-size:12px;color:var(--muted)}
.search{position:absolute;right:70px;top:42px}
.search .btn{display:block;background:var(--accent);color:var(--white);font-size:12px;padding:4px 14px;font-weight:700}
.global-nav{height:49px;background:var(--white);border-top:1px solid var(--line);border-bottom:3px solid var(--green);display:flex;justify-content:center}
.global-nav a{width:150px;text-align:center;line-height:45px;font-size:14px;color:var(--text);text-decoration:none;border-right:1px solid var(--line)}
.global-nav a:first-child{border-left:1px solid var(--line)}
.hero{background:var(--green);height:540px;position:relative}
.ph{display:block}
.hero-left{position:absolute;left:0;top:0;width:290px;height:390px;background:linear-gradient(135deg,#2a1f14,#a8561e 55%,#f0b34a)}
.hero-main{position:absolute;left:290px;top:0;width:620px;height:390px;background:radial-gradient(circle at 50% 45%,#d8482e,#7a2a1d 60%,#2a2a22)}
.hero-right{position:absolute;left:910px;top:0;width:290px;height:390px;background:linear-gradient(160deg,#f4f5f6,#c7ccd0 60%,#8d9490)}
.thumbs{position:absolute;left:20px;top:408px;display:flex;gap:12px}
.thumbs .ph{width:222px;height:112px;border:3px solid var(--white)}
.t1{background:linear-gradient(135deg,#2b1a10,#d88c2d)}
.t2{background:radial-gradient(circle,#c9432b,#4a2318)}
.t3{background:linear-gradient(180deg,#e9ecef,#9aa39a)}
.t4{background:linear-gradient(180deg,#dfe3e6,#a5adb1)}
.t5{background:linear-gradient(135deg,#7a1f1c,#e0b48a)}
.section{width:1060px;margin:0 auto;position:relative}
.section-title{display:flex;align-items:center;gap:18px;font-size:17px;font-weight:500;color:var(--text);justify-content:center;height:40px}
.section-title::before,.section-title::after{content:"";flex:1;height:1px;background:var(--line)}
.news{padding-top:36px}
.news-list{display:flex;gap:40px;margin-top:18px;justify-content:center}
.news-card{width:300px}
.news-card .ph{width:300px;height:180px}
.n1{background:linear-gradient(160deg,#e6e2d8,#8a7a66)}
.n2{background:var(--white);border:1px solid var(--line)}
.n3{background:linear-gradient(150deg,#d8541d,#f2a23a 50%,#5d3a1d)}
.n2-inner{display:flex;height:100%;align-items:center;justify-content:center;font-size:24px;color:var(--green-dark);font-weight:700}
.news-meta{margin-top:10px;display:flex;gap:8px;align-items:center;font-size:11px;color:var(--muted)}
.tag{background:var(--accent);color:var(--white);font-size:10px;padding:0 6px;font-weight:700}
.news-title{margin-top:6px;font-size:15px;line-height:1.6;font-weight:500}
.contents{padding-top:40px}
.content-grid{display:grid;grid-template-columns:repeat(3,300px);gap:16px 40px;justify-content:center;margin-top:20px}
.tile{height:200px;position:relative}
.tile .label{position:absolute;left:14px;bottom:14px;font-family:"Noto Serif JP",serif;font-weight:700;font-size:34px;color:var(--white);text-shadow:0 2px 6px rgba(0,0,0,.5)}
.c1{background:linear-gradient(180deg,#eef0f2,#9aa49b)}
.c2{background:linear-gradient(135deg,#1d140d,#c66a22)}
.c3{background:linear-gradient(180deg,#cfd6da,#6f7a6e)}
.c4{background:linear-gradient(180deg,#b8d2e8,#c9a24a)}
.c5{background:radial-gradient(circle,#c8402b,#3e1d14)}
.c6{background:linear-gradient(180deg,#9fc1da,#5b6f52)}
.seasons{padding-top:34px}
.season-row{display:flex;gap:20px;justify-content:center;margin-top:18px}
.season{width:220px;height:140px;position:relative}
.season .label{position:absolute;left:12px;bottom:10px;width:44px;height:44px;background:rgba(255,255,255,.9);border-radius:50%;text-align:center;line-height:44px;font-family:"Noto Serif JP",serif;font-weight:700;font-size:24px}
.s1{background:linear-gradient(135deg,#c7d9f0,#b48ad0)}.s1 .label{color:#c0467a}
.s2{background:linear-gradient(135deg,#4f7fcf,#8ab4e6)}.s2 .label{color:#2f65b5}
.s3{background:linear-gradient(135deg,#f0a32c,#c9391e)}.s3 .label{color:#c9391e}
.s4{background:linear-gradient(180deg,#dfe4e8,#8f9aa0)}.s4 .label{color:#5b6b76}
.pr{padding-top:40px}
.pr-grid{display:grid;grid-template-columns:repeat(4,230px);gap:40px 40px;justify-content:center;margin-top:24px}
.banner{height:76px;background:var(--white);border:1px solid var(--line);display:flex;align-items:center;justify-content:center}
.banner i{display:block;width:160px;height:44px;border-radius:4px}
.b-green i{background:var(--green-light)}
.b-red i{background:#f3dcd8}
.b-gold i{background:#f3ead0}
.b-blue i{background:#dde7f2}
.site-footer{position:absolute;left:0;bottom:0;width:1200px;height:70px;background:var(--green);color:var(--white);font-size:12px;display:flex;align-items:center;justify-content:center}
</style>
</head>
<body>
<header class="site-header">
  <p class="brand-sub">ものづくりと自然のまち　燕川観光ネット</p>
  <div class="brand"><span class="brand-mark"></span><span class="brand-name">燕川たびナビ</span></div>
  <div class="util"><span>文字サイズ</span><span class="size"><span>拡大</span><span>標準</span></span></div>
  <nav class="util-links"><span>サイトマップ</span><span>アクセシビリティ</span><span>リンク集</span></nav>
  <div class="search"><span class="btn">検索</span></div>
</header>
<nav class="global-nav">
  <a>燕川とは</a><a>イベント情報</a><a>観光情報</a><a>工場情報</a><a>温泉・宿泊情報</a><a>モデルコース</a><a>交通案内</a>
</nav>
<section class="hero">
  <div class="ph hero-left" role="img" aria-label="鍛冶の火花の写真"></div>
  <div class="ph hero-main" role="img" aria-label="祭りの演者の写真"></div>
  <div class="ph hero-right" role="img" aria-label="雪景色の寺の写真"></div>
  <div class="thumbs">
    <div class="ph t1" role="img" aria-label="火花の写真"></div>
    <div class="ph t2" role="img" aria-label="祭りの写真"></div>
    <div class="ph t3" role="img" aria-label="雪の寺の写真"></div>
    <div class="ph t4" role="img" aria-label="雪景色の写真"></div>
    <div class="ph t5" role="img" aria-label="寺院内部の写真"></div>
  </div>
</section>
<section class="section news">
  <h2 class="section-title">新着情報</h2>
  <div class="news-list">
    <article class="news-card"><div class="ph n1" role="img" aria-label="工房見学の写真"></div><p class="news-meta">2020 / 02 / 20 <span class="tag">NEW</span></p><p class="news-title">タイトルが入りますタイトルが入ります</p></article>
    <article class="news-card"><div class="ph n2"><div class="n2-inner">燕川たびナビ</div></div><p class="news-meta">2020 / 02 / 20 <span class="tag">NEW</span></p><p class="news-title">タイトルが入りますタイトルが入ります</p></article>
    <article class="news-card"><div class="ph n3" role="img" aria-label="紅葉の写真"></div><p class="news-meta">2020 / 02 / 20 <span class="tag">NEW</span></p><p class="news-title">タイトルが入りますタイトルが入ります</p></article>
  </div>
</section>
<section class="section contents">
  <h2 class="section-title">観光コンテンツ</h2>
  <div class="content-grid">
    <div class="tile c1" role="img" aria-label="雪の寺の写真"><span class="label">観光情報</span></div>
    <div class="tile c2" role="img" aria-label="工場の火花の写真"><span class="label">工場情報</span></div>
    <div class="tile c3" role="img" aria-label="温泉の湯けむりの写真"><span class="label">温泉・宿泊</span></div>
    <div class="tile c4" role="img" aria-label="田園風景の写真"><span class="label">モデルコース</span></div>
    <div class="tile c5" role="img" aria-label="祭りの写真"><span class="label">イベント情報</span></div>
    <div class="tile c6" role="img" aria-label="駅と線路の写真"><span class="label">交通案内</span></div>
  </div>
</section>
<section class="section seasons">
  <h2 class="section-title">燕川の四季</h2>
  <div class="season-row">
    <div class="season s1" role="img" aria-label="春の花の写真"><span class="label">春</span></div>
    <div class="season s2" role="img" aria-label="夏の紫陽花の写真"><span class="label">夏</span></div>
    <div class="season s3" role="img" aria-label="秋の紅葉の写真"><span class="label">秋</span></div>
    <div class="season s4" role="img" aria-label="冬の雪景色の写真"><span class="label">冬</span></div>
  </div>
</section>
<section class="section pr">
  <h2 class="section-title">PR</h2>
  <div class="pr-grid">
    <div class="banner b-green"><i></i></div><div class="banner b-blue"><i></i></div><div class="banner b-blue"><i></i></div><div class="banner b-green"><i></i></div>
    <div class="banner b-red"><i></i></div><div class="banner b-green"><i></i></div><div class="banner b-gold"><i></i></div><div class="banner b-gold"><i></i></div>
    <div class="banner b-green"><i></i></div><div class="banner b-blue"><i></i></div><div class="banner b-green"><i></i></div><div class="banner b-red"><i></i></div>
  </div>
</section>
<footer class="site-footer">燕川観光ネット事務局　〒000-0000 架空県燕川市中央1-2-3　TEL 000-000-0000</footer>
</body>
</html>
```